Presentation Folder, Business Card, Letterhead and Envelope design

We are a dental clinic that will open in August and we are looking for a professional graphic designer to create our Business Card, Presentation Folder, Letterhead, Notepad and envelopes.

The brand NovaGrin must reflect a sense of quality and sophistication, marketed for middle-class consumers.
Our preference is for quality and refined materials, where less is more.
Attached the logo

```html
<!DOCTYPE html>
<html lang="en">
<head>
<meta charset="utf-8">
<title>NovaGrin Stationery</title>
<link rel="stylesheet" href="https://fonts.googleapis.com/css2?family=Josefin+Sans:wght@300;400&family=Montserrat:wght@400;500;600;700&display=swap">
<style>
  :root {
    --bg: #f1f1f1;
    --slate: #5a5a5a;
    --slate-dark: #4a4a4a;
    --maroon: #6e1515;
    --paper: #ffffff;
    --ink: #3c3c3c;
    --faint: #ececec;
    --rule: #9a9a9a;
    --shadow: 3px 4px 7px rgba(0,0,0,.35);
    --brand-font: "Josefin Sans", sans-serif;
    --body-font: "Montserrat", sans-serif;
  }
  * { box-sizing: border-box; margin: 0; padding: 0; }
  html, body { width: 1000px; height: 1200px; overflow: hidden; }
  body { background: var(--bg); position: relative; font-family: var(--body-font); color: var(--ink); }

  .sheet { position: absolute; box-shadow: var(--shadow); overflow: hidden; }
  .brand-name { position: absolute; font-family: var(--brand-font); font-weight: 300; white-space: nowrap; text-transform: uppercase; }
  .brand-square { position: absolute; }
  .web { position: absolute; font-weight: 700; color: var(--maroon); letter-spacing: 1.6px; font-size: 9.5px; white-space: nowrap; }
  .band-top { position: absolute; left: 0; top: 0; right: 0; height: 6px; background: var(--maroon); }
  .band-bottom { position: absolute; left: 0; bottom: 0; right: 0; background: var(--slate); }
  .faint-panel { position: absolute; background: var(--faint); }

  /* Presentation folder */
  .folder { left: 48px; top: 57px; width: 435px; height: 612px; background: var(--slate); }
  .folder-frame { position: absolute; inset: 14px; border: 1px solid #e6e6e6; }
  .folder .brand-square { left: 169px; top: 215px; width: 96px; height: 116px; background: var(--paper); }
  .folder .brand-name { left: 0; right: 0; top: 356px; text-align: center; font-size: 46px; letter-spacing: 5px; color: var(--paper); }
  .folder .web { left: 0; right: 0; top: 559px; text-align: center; }

  /* Letterhead */
  .letterhead { left: 519px; top: 57px; width: 434px; height: 612px; background: var(--paper); }
  .letterhead .brand-square { left: 193px; top: 23px; width: 48px; height: 48px; background: var(--slate); }
  .letterhead .brand-name { left: 0; right: 0; top: 82px; text-align: center; font-size: 21px; letter-spacing: 3px; color: var(--slate); }
  .letterhead .faint-panel { left: 127px; top: 235px; width: 180px; height: 180px; }
  .letterhead-footer { position: absolute; left: 29px; right: 29px; top: 569px; height: 17px; border-top: 1px solid var(--rule); border-bottom: 1px solid var(--rule); font-size: 9px; font-weight: 500; letter-spacing: .6px; text-align: center; line-height: 15px; color: #222; }
  .letterhead .web { left: 0; right: 0; top: 591px; text-align: center; }
  .letterhead .band-bottom { height: 7px; }

  /* Envelope back */
  .envelope-back { left: 37px; top: 724px; width: 448px; height: 208px; background: var(--paper); }
  .envelope-back .brand-square { left: 74px; top: 27px; width: 36px; height: 36px; background: var(--slate); }
  .envelope-back .brand-name { left: 36px; top: 71px; font-size: 16px; letter-spacing: 2px; color: var(--slate); }
  .envelope-back .faint-panel { left: 263px; top: 28px; width: 147px; height: 154px; }
  .envelope-address { position: absolute; left: 36px; top: 162px; width: 112px; font-size: 6.5px; font-weight: 600; text-align: center; line-height: 9.5px; color: #222; }
  .envelope-back .band-bottom { height: 5px; }

  /* Envelope front */
  .envelope-front { left: 519px; top: 724px; width: 447px; height: 209px; background: var(--paper); }
  .envelope-flap { position: absolute; left: 0; top: 0; }
  .envelope-front .brand-square { left: 207px; top: 8px; width: 34px; height: 36px; background: var(--paper); }
  .envelope-front .web { left: 0; right: 0; top: 174px; text-align: center; font-size: 9px; }

  /* Business card front */
  .card-front { left: 123px; top: 1000px; width: 276px; height: 170px; background: var(--slate); }
  .card-frame { position: absolute; inset: 8px; border: 1px solid #e6e6e6; border-radius: 8px; }
  .card-front .brand-square { left: 111px; top: 32px; width: 54px; height: 66px; background: var(--paper); }
  .card-front .brand-name { left: 0; right: 0; top: 110px; text-align: center; font-size: 26px; letter-spacing: 3px; color: var(--paper); }

  /* Business card back */
  .card-back { left: 626px; top: 999px; width: 277px; height: 170px; background: var(--paper); }
  .card-back .brand-square { left: 29px; top: 28px; width: 27px; height: 27px; background: var(--slate); }
  .card-back .brand-name { left: 62px; top: 26px; font-size: 28px; letter-spacing: 3px; color: var(--slate); }
  .card-back .band-bottom { height: 4px; }
  .holder { position: absolute; right: 137px; top: 90px; text-align: right; }
  .holder-name { font-size: 12px; font-weight: 500; color: #222; }
  .holder-role { font-size: 7.5px; color: var(--maroon); margin-top: 1px; }
  .holder-address { font-size: 7px; line-height: 10px; color: #444; margin-top: 9px; }
  .card-divider { position: absolute; left: 146px; top: 82px; width: 1px; height: 70px; background: #cfcfcf; }
  .contact-list { position: absolute; left: 154px; top: 85px; list-style: none; }
  .contact-list li { display: flex; align-items: center; height: 17px; font-size: 7.5px; color: #555; }
  .contact-list svg { width: 11px; height: 11px; margin-right: 7px; }
</style>
</head>
<body>

  <section class="sheet folder">
    <div class="folder-frame"></div>
    <div class="brand-square"></div>
    <div class="brand-name">NovaGrin</div>
    <div class="web">WWW.NOVAGRIN.COM</div>
  </section>

  <section class="sheet letterhead">
    <div class="band-top"></div>
    <div class="brand-square"></div>
    <div class="brand-name">NovaGrin</div>
    <div class="faint-panel"></div>
    <div class="letterhead-footer">01, NovaGrin Clinic, Your Street, Your Country Code - 12345</div>
    <div class="web">WWW.NOVAGRIN.COM</div>
    <div class="band-bottom"></div>
  </section>

  <section class="sheet envelope-back">
    <div class="band-top"></div>
    <div class="brand-square"></div>
    <div class="brand-name">NovaGrin</div>
    <div class="faint-panel"></div>
    <p class="envelope-address">01, NovaGrin Clinic, Your Street,<br>Your Country Code - 12345</p>
    <div class="band-bottom"></div>
  </section>

  <section class="sheet envelope-front">
    <svg class="envelope-flap" width="447" height="50" viewBox="0 0 447 50">
      <polygon points="0,0 447,0 400,48 47,48" fill="#5a5a5a"/>
    </svg>
    <div class="brand-square"></div>
    <div class="web">WWW.NOVAGRIN.COM</div>
  </section>

  <section class="sheet card-front">
    <div class="card-frame"></div>
    <div class="brand-square"></div>
    <div class="brand-name">NovaGrin</div>
  </section>

  <section class="sheet card-back">
    <div class="band-top"></div>
    <div class="brand-square"></div>
    <div class="brand-name">NovaGrin</div>
    <div class="holder">
      <div class="holder-name">YOUR DESIGN</div>
      <div class="holder-role">Managing Director</div>
      <div class="holder-address">01, NovaGrin Clinic, Your Street,<br>Your Country Code - 12345</div>
    </div>
    <div class="card-divider"></div>
    <ul class="contact-list">
      <li><svg viewBox="0 0 12 12"><circle cx="6" cy="6" r="5.5" fill="none" stroke="#6e1515"/><path d="M3.5 5 Q6 2.5 8.5 5 L7.5 6 L6.8 5.3 H5.2 L4.5 6 Z M4.5 7 H7.5 V8.8 H4.5 Z" fill="#6e1515"/></svg>012 3456 789</li>
      <li><svg viewBox="0 0 12 12"><circle cx="6" cy="6" r="5.5" fill="none" stroke="#6e1515"/><rect x="3.5" y="3" width="5" height="2.5" fill="#6e1515"/><rect x="3" y="6" width="6" height="3" fill="#6e1515"/></svg>012 3456 780</li>
      <li><svg viewBox="0 0 12 12"><circle cx="6" cy="6" r="5.5" fill="none" stroke="#6e1515"/><rect x="3.2" y="4" width="5.6" height="4" fill="none" stroke="#6e1515" stroke-width=".9"/><path d="M3.2 4 L6 6.2 L8.8 4" fill="none" stroke="#6e1515" stroke-width=".9"/></svg>info@novagrin.com</li>
      <li><svg viewBox="0 0 12 12"><circle cx="6" cy="6" r="5.5" fill="none" stroke="#6e1515"/><circle cx="6" cy="6" r="3" fill="none" stroke="#6e1515" stroke-width=".8"/><path d="M3 6 H9 M6 3 V9" stroke="#6e1515" stroke-width=".7"/></svg>www.novagrin.com</li>
    </ul>
    <div class="band-bottom"></div>
  </section>

</body>
</html>
```